Tova Brisk Fitness Coaching Project

I am a personal trainer based in London. My services include one-on-one PT sessions, bootcamps.
I would like the design to be minimalistic. With light colours: white, pink, purple.
I specialise in weight loss, flexibility, mobility.

Tova Penrick
Personal Trainer
Email: tova.penrick@mailgrove.net
tel: 07500 918 243
Instagram: Tova Brisk

Target Market(s)

adults, mostly females (age 18-50).

Industry/Entity Type

Fitness

Contact Information for Business Card

Tova Penrick
Personal Trainer
tel: 07500 918 243
Instagram: Tova Brisk

Font styles to use
Serif

Colors
eea4c8
fbd4d5
fdf9cf
cfeae6
cee9f5

Requirements
Nice to have
• minimalistic style
• easy to read and remember

```html
<!DOCTYPE html>
<html lang="en">
<head>
<meta charset="utf-8">
<title>Tova Penrick – Personal Trainer Business Card</title>
<link rel="stylesheet" href="https://fonts.googleapis.com/css2?family=Tinos:wght@400&display=swap">
<style>
  :root {
    --backdrop: #2e2e30;
    --card-pink: #fcd3d6;
    --cream: #fbf7cf;
    --orchid: #e9a6cf;
    --white: #ffffff;
    --ink: #2a2326;
    --plum: #b0628f;
    --icon: #a05a86;
    --portrait-dark: #2b3127;
    --portrait-warm: #8a5a3c;
    --coral: #e8735f;
    --stone: #8f9298;
    --magenta: #e4187a;
    --teal: #2fb3c4;
  }
  * { box-sizing: border-box; margin: 0; padding: 0; }
  html, body { width: 1200px; height: 900px; overflow: hidden; }
  body {
    background: var(--backdrop);
    font-family: "Tinos", "Times New Roman", serif;
    position: relative;
  }
  .card {
    position: absolute;
    width: 680px;
    height: 390px;
    border-radius: 22px;
    overflow: hidden;
    box-shadow: 0 14px 30px rgba(0,0,0,0.45);
  }
  .card-art { position: absolute; inset: 0; width: 100%; height: 100%; display: block; }
  .card-back { left: 480px; top: 40px; }
  .card-front { left: 40px; top: 470px; background: var(--card-pink); }

  .identity { position: absolute; left: 42px; top: 44px; }
  .identity-name { font-size: 32px; font-weight: 400; color: var(--ink); letter-spacing: 0.3px; line-height: 1; }
  .identity-role { font-size: 13px; color: var(--plum); margin-top: 4px; }

  .contact-list { position: absolute; left: 40px; top: 220px; list-style: none; }
  .contact-item {
    display: flex; align-items: center; gap: 12px;
    font-size: 17px; color: var(--ink); height: 30px;
  }
  .contact-icon {
    width: 22px; height: 22px; border-radius: 50%;
    background: var(--icon);
    display: flex; align-items: center; justify-content: center;
    flex: none;
  }
  .contact-glyph { width: 12px; height: 12px; display: block; }
</style>
</head>
<body>

  <section class="card card-back">
    <svg class="card-art" viewBox="0 0 680 390" preserveAspectRatio="none">
      <defs>
        <linearGradient id="streetScene" x1="0" y1="0" x2="0" y2="1">
          <stop offset="0" stop-color="#e8735f"/>
          <stop offset="0.55" stop-color="#c65a4c"/>
          <stop offset="1" stop-color="#8f9298"/>
        </linearGradient>
        <linearGradient id="muralScene" x1="0" y1="0" x2="0" y2="1">
          <stop offset="0" stop-color="#e4187a"/>
          <stop offset="0.45" stop-color="#d63c8a"/>
          <stop offset="0.6" stop-color="#2fb3c4"/>
          <stop offset="1" stop-color="#1f6f78"/>
        </linearGradient>
      </defs>
      <g role="img" aria-label="Photo of the trainer doing a handstand cartwheel in front of a coral street wall">
        <rect x="0" y="0" width="420" height="390" fill="url(#streetScene)"/>
      </g>
      <g role="img" aria-label="Photo of the trainer leaping in a pink top before a pink and teal painted wall">
        <path d="M330 0 H680 V390 H300 C360 300 320 160 330 0 Z" fill="url(#muralScene)"/>
      </g>
      <rect x="0" y="378" width="300" height="12" fill="#e9a6cf"/>
    </svg>
  </section>

  <section class="card card-front">
    <svg class="card-art" viewBox="0 0 680 390" preserveAspectRatio="none">
      <defs>
        <linearGradient id="portraitFade" x1="0" y1="0" x2="1" y2="0">
          <stop offset="0" stop-color="#fbf7cf"/>
          <stop offset="0.38" stop-color="#fbf7cf"/>
          <stop offset="0.62" stop-color="#2b3127"/>
          <stop offset="0.82" stop-color="#8a5a3c"/>
          <stop offset="1" stop-color="#2b3127"/>
        </linearGradient>
      </defs>
      <g role="img" aria-label="Portrait photo of the smiling trainer with long curly hair">
        <path d="M0 0 H680 V315 C580 345 470 320 390 260 C310 195 240 110 0 108 Z" fill="url(#portraitFade)"/>
      </g>
      <path d="M0 118 C230 120 300 205 380 272 C460 340 580 360 680 330" fill="none" stroke="#e9a6cf" stroke-width="12"/>
      <path d="M0 134 C220 136 290 222 370 290 C450 356 580 372 680 345" fill="none" stroke="#ffffff" stroke-width="10"/>
      <path d="M0 146 C210 150 280 236 360 304 C440 368 580 384 680 362" fill="none" stroke="#e9a6cf" stroke-width="4"/>
    </svg>

    <header class="identity">
      <h1 class="identity-name">Tova Penrick</h1>
      <p class="identity-role">Personal Trainer</p>
    </header>

    <ul class="contact-list">
      <li class="contact-item">
        <span class="contact-icon">
          <svg class="contact-glyph" viewBox="0 0 24 24"><path d="M6.6 10.8a15 15 0 0 0 6.6 6.6l2.2-2.2a1 1 0 0 1 1-.25 11 11 0 0 0 3.6.6 1 1 0 0 1 1 1V20a1 1 0 0 1-1 1A17 17 0 0 1 3 4a1 1 0 0 1 1-1h3.5a1 1 0 0 1 1 1 11 11 0 0 0 .6 3.6 1 1 0 0 1-.25 1z" fill="#fff"/></svg>
        </span>
        07500 918 243
      </li>
      <li class="contact-item">
        <span class="contact-icon">
          <svg class="contact-glyph" viewBox="0 0 24 24"><rect x="3" y="5" width="18" height="14" rx="1.5" fill="none" stroke="#fff" stroke-width="2.2"/><path d="M3.5 6 12 13l8.5-7" fill="none" stroke="#fff" stroke-width="2.2"/></svg>
        </span>
        tova.penrick@mailgrove.net
      </li>
      <li class="contact-item">
        <span class="contact-icon">
          <svg class="contact-glyph" viewBox="0 0 24 24"><circle cx="12" cy="12" r="5" fill="#fff"/></svg>
        </span>
        Tova Brisk
      </li>
    </ul>
  </section>

</body>
</html>
```